Business Card Design

We are looking for a business card designed for our landscaping company. We do landscaping installation & Maintenance Services. We would like to see designs that have basic landscaping in background. We also think it is important to have both of our names and phone numbers on the card. We need something that stands out a little whether it is shape of the card or thickness or design.

Industry/Entity Type

Business

Contact Information for Business Card

Pale Ridge Yardworks, paleridgeyardworks@mailbrook.net, Dale Purvine 555-213-7690, Martin Kolbey 555-864-1037

```html
<!DOCTYPE html>
<html lang="en">
<head>
<meta charset="utf-8">
<title>Pale Ridge Yardworks – Business Card</title>
<link href="https://fonts.googleapis.com/css2?family=Roboto:wght@300;400;700;900&display=swap" rel="stylesheet">
<style>
  :root {
    --page-bg: #eeece8;
    --card-white: #ffffff;
    --grass-dark: #3f8f22;
    --grass-mid: #5aaa35;
    --grass-light: #7fc454;
    --accent-green: #4c9a2a;
    --edge-gray: #9a9a9a;
    --edge-gray-light: #d6d6d6;
    --ink: #444444;
    --ink-soft: #666666;
  }
  * { margin: 0; padding: 0; box-sizing: border-box; }
  html, body {
    width: 1200px; height: 900px; overflow: hidden;
    background: var(--page-bg);
    font-family: "Roboto", Arial, sans-serif;
  }
  .card {
    position: absolute; left: 100px; top: 164px;
    width: 1000px; height: 572px;
    background: linear-gradient(90deg, var(--card-white) 0%, var(--card-white) 75%, var(--edge-gray-light) 88%, var(--edge-gray) 100%);
    box-shadow: 0 14px 30px rgba(0,0,0,0.18);
    overflow: hidden;
  }
  .card__edge-stripe {
    position: absolute; left: 14px; top: 90px; width: 10px; height: 400px;
    background: var(--accent-green);
  }
  .grass-band {
    position: absolute; left: 430px; right: 0;
    background: linear-gradient(90deg, var(--grass-mid) 0%, var(--grass-light) 60%, var(--edge-gray) 100%);
  }
  .grass-band--top { top: 0; height: 70px; }
  .grass-band--bottom { bottom: 0; height: 50px; }
  .grass-panel {
    position: absolute; left: 36px; top: 0; width: 420px; height: 572px;
    background: radial-gradient(ellipse at 40% 40%, var(--grass-light) 0%, var(--grass-mid) 55%, var(--grass-dark) 100%);
  }
  .brand {
    position: absolute; left: 36px; top: 140px; width: 420px;
    text-align: center; color: var(--card-white);
  }
  .brand__name {
    font-weight: 900; font-size: 58px; line-height: 1.05;
    letter-spacing: -0.5px;
  }
  .brand__rule {
    width: 330px; height: 2px; margin: 26px auto 22px;
    background: var(--card-white);
  }
  .brand__services {
    font-weight: 300; font-size: 30px; line-height: 1.2;
  }
  .contacts {
    position: absolute; left: 486px; top: 120px; width: 400px;
    color: var(--ink);
  }
  .contact { margin-bottom: 42px; }
  .contact__name {
    display: flex; align-items: center; gap: 12px;
    font-size: 24px; font-weight: 400; color: var(--ink-soft);
  }
  .contact__dot {
    width: 14px; height: 14px; flex: none;
    border-radius: 50%;
    background: var(--accent-green);
  }
  .contact__phone { font-size: 28px; margin-top: 8px; }
  .email { font-size: 21px; color: var(--ink-soft); }
</style>
</head>
<body>
  <div class="card">
    <div class="card__edge-stripe"></div>
    <div class="grass-band grass-band--top" role="img" aria-label="Strip of lawn grass texture"></div>
    <div class="grass-band grass-band--bottom" role="img" aria-label="Strip of lawn grass texture"></div>
    <div class="grass-panel" role="img" aria-label="Close-up photograph of green lawn grass"></div>

    <div class="brand">
      <div class="brand__name">Pale Ridge<br>Yardworks</div>
      <div class="brand__rule"></div>
      <div class="brand__services">landscaping installation &amp;<br>Maintenance Services</div>
    </div>

    <div class="contacts">
      <div class="contact">
        <div class="contact__name">
          <span class="contact__dot" aria-hidden="true"></span>
          Dale Purvine
        </div>
        <div class="contact__phone">555-213-7690</div>
      </div>
      <div class="contact">
        <div class="contact__name">
          <span class="contact__dot" aria-hidden="true"></span>
          Martin Kolbey
        </div>
        <div class="contact__phone">555-864-1037</div>
      </div>
      <div class="email">paleridgeyardworks@mailbrook.net</div>
    </div>
  </div>
</body>
</html>
```